Tito - Lumora Estudos

2x Design Concepts for the home page and interior pages based on the attached brief and powerpoint presentation.

Colours: see 2.1 logo and heading for logo colours and website colours

Home Page: (please see attached file)
1)Logo to appear in the top left, heading to include telephone numbers and a best price (credibility stamp) - see 2.1
2)the toolbar is to be centered at the top. Emphasis must be placed on the 5 easy steps to study english in Australia - see 2.2
3) modules. 5x modules required in the home page for: home page image rotator, online quote tool, enquiry form, best deals, quick links (there are 2 examples for the quick links module - open to suggestions) - see 2.3
4) footer. the footer is to include partner logos with hyperlinks to the partner websites. with a copywright section at the base - see 2.4
5) 2.5 is the basic idea - open to design suggestions. The website objective is to submit an online quote or contact Lumora Estudos.

Internal Page: - see 3-
open to all suggestion. Require a lot of space for internal custom design concepts (these are taking place inhouse). The interior page must have a side module toolbar to include:
1) a modified online quote tool
2) modified enquiry form
3) modified quick links section

Target Market(s)

target market is young (17-30yrs) Brazilians looking to study English in Australia or continue studying English in Australia that can also acquire visa sponsorship.

The buyer will be the parents of the students. the design must appeal to both markets.

Number of Pages Required

2 pages

Requirements
Must have
• see project overview
2x design concepts for the home page and interior page
professional, clean, simple and easy to navigate

```html
<!DOCTYPE html>
<html lang="en">
<head>
<meta charset="utf-8">
<title>Lumora Estudos – Study English in Australia</title>
<link href="https://fonts.googleapis.com/css2?family=Arimo:wght@400;700&display=swap" rel="stylesheet">
<style>
:root{
  --green:#2f6a50;
  --green-dark:#245a42;
  --green-light:#5a9b79;
  --blue:#1e58a0;
  --blue-dark:#174a8a;
  --blue-soft:#89a8cf;
  --orange:#e58a42;
  --orange-light:#f4b37a;
  --panel:#e7ebe9;
  --text:#2b2b2b;
  --muted:#8c8c8c;
  --rule:#d5d5d5;
  --gold:#e0a81c;
  --white:#ffffff;
}
*{box-sizing:border-box;margin:0;padding:0}
html,body{width:1200px;height:1101px;overflow:hidden;background:var(--white)}
body{font-family:"Arimo",Arial,sans-serif;color:var(--text);position:relative}

.brand{position:absolute;left:120px;top:44px;display:flex;align-items:center;gap:12px}
.brand-mark{width:22px;height:22px;background:var(--orange);border-radius:50%}
.brand-name{font-size:32px;font-weight:700;color:var(--green)}

.phones{position:absolute;left:788px;top:42px;display:flex;flex-direction:column;gap:14px}
.phone{display:flex;align-items:center;gap:8px;font-size:20px;font-weight:700;color:#6a6a6a}
.flag{width:40px;height:24px;border-radius:3px}
.flag.au{background:var(--blue-dark)}
.flag.br{background:#3d9a3d}
.stamp{position:absolute;left:962px;top:4px;width:122px;height:122px}

.nav{position:absolute;left:110px;top:138px;width:981px;height:39px;display:flex;border-radius:4px;overflow:hidden;
  background:linear-gradient(var(--green-light),var(--green-dark))}
.nav a{display:flex;align-items:center;justify-content:center;gap:8px;color:var(--white);font-size:17px;text-decoration:none;
  border-right:1px solid rgba(255,255,255,.25)}
.nav a:last-child{border-right:0}
.nav .home{color:#f1d54a}
.nav .blue{background:linear-gradient(#2b6ab6,var(--blue-dark))}
.nav .soft{background:linear-gradient(#9cb8da,#7b9dc7)}
.nav .caret{font-size:10px}

.hero{position:absolute;left:111px;top:195px;width:532px;height:354px;
  background:linear-gradient(120deg,#d6d9de 0%,#e9c27a 35%,#b7bcc4 65%,#e2e5e8 100%)}

.quote{position:absolute;left:651px;top:196px;width:440px;height:353px;background:var(--green);border-radius:4px;color:var(--white)}
.quote h2{position:absolute;left:33px;top:24px;font-size:26px;font-weight:700;display:flex;align-items:center;gap:10px}
.quote .label{position:absolute;font-size:19px}
.cities{position:absolute;left:72px;top:116px;list-style:none;font-size:15px;line-height:18.3px}
.cities li{display:flex;align-items:center;gap:10px}
.cities li::before{content:"";width:11px;height:11px;border-radius:50%;background:var(--white)}
.duration{position:absolute;left:272px;top:118px;width:125px;height:22px;background:var(--white)}
.btn{display:flex;align-items:center;justify-content:center;color:var(--white);border-radius:5px;
  background:linear-gradient(var(--orange-light),var(--orange));border:1px solid #d6783a}
.quote .btn{position:absolute;left:72px;top:276px;width:292px;height:53px;font-size:20px;font-weight:700;text-shadow:0 1px 1px rgba(0,0,0,.3)}

.col h3{font-size:26px;font-weight:700;color:var(--green);margin-bottom:18px}
.col{position:absolute;top:568px}

.deals{left:109px;width:301px}
.deal{display:flex;align-items:center;height:43.3px;border-bottom:1px solid var(--rule);font-size:15px}
.tag{position:relative;width:86px;height:34px;margin-right:22px;background:linear-gradient(var(--green-light),var(--green-dark));
  border-radius:3px;color:var(--white);font-size:13px;font-weight:700;display:flex;align-items:center;justify-content:center}
.tag::after{content:"";position:absolute;right:-9px;top:11px;border:6px solid transparent;border-left:9px solid var(--green)}
.more{display:flex;justify-content:flex-end;align-items:center;gap:5px;font-size:13px;color:var(--green)}
.more::after{content:"";border:5px solid transparent;border-left:8px solid var(--green);border-right:0}
.deals .more{margin-top:14px}

.divider{position:absolute;top:573px;width:1px;height:392px;background:var(--rule)}

.ask{left:447px;width:268px}
.ask-box{background:var(--panel);border-radius:4px;height:333px;padding:26px 19px 0 14px;font-size:15px}
.ask-box p{margin-bottom:40px}
.field{display:flex;align-items:center;justify-content:space-between;height:32.6px}
.field span{margin-right:8px}
.field i{display:block;height:24px;background:var(--white);flex:1;max-width:178px}
.ask .btn{width:166px;height:38px;margin:52px 0 0 41px;font-size:19px}

.links{left:742px;width:349px}
.link-item{display:flex;gap:16px;height:131px}
.thumb{width:77px;height:77px;background:var(--panel);border-radius:3px;flex:none}
.link-item h4{font-size:15px;font-weight:700;margin-top:4px}
.link-item p{font-size:13px;line-height:15px;width:250px;overflow:hidden;white-space:nowrap}
.link-item .more{margin-top:9px}

.footer{position:absolute;left:111px;top:1016px;width:979px;height:73px;background:var(--panel);color:var(--muted);font-size:12.5px}
.footer .copy{position:absolute;left:24px;top:20px;line-height:20px}
.footer .copy a{color:var(--muted);text-decoration:none}
.footer .sep{margin:0 9px}
.partner{position:absolute;top:20px;height:32px;background:#b9c0d6;border-radius:4px}
</style>
</head>
<body>

<header>
  <div class="brand"><span class="brand-mark"></span><span class="brand-name">Lumora Estudos</span></div>
  <div class="phones">
    <div class="phone"><span class="flag au"></span>0 800 555 010</div>
    <div class="phone"><span class="flag br"></span>1 800 555 020</div>
  </div>
  <svg class="stamp" viewBox="0 0 122 122" aria-hidden="true">
    <polygon fill="var(--gold)" points="61,2 70,18 87,8 89,27 108,25 101,43 119,50 104,62 117,76 99,81 104,100 85,98 79,117 64,105 50,119 43,101 24,106 26,87 7,82 18,66 4,53 22,45 16,27 35,29 38,10 54,20"/>
  </svg>
  <nav class="nav">
    <a class="home" style="width:96px">Home</a>
    <a style="width:128px">Promotions</a>
    <a class="blue" style="width:107px">Cities <span class="caret">▼</span></a>
    <a class="blue" style="width:117px">Schools <span class="caret">▼</span></a>
    <a class="soft" style="width:118px">Air Tickets</a>
    <a class="soft" style="width:85px">Visa</a>
    <a class="soft" style="width:139px">Final Details</a>
    <a style="width:108px">Contact</a>
    <a style="width:83px">Blog</a>
  </nav>
</header>

<main>
  <div class="hero" role="img" aria-label="Photo of smiling young students studying together at a classroom desk"></div>

  <section class="quote">
    <h2><svg width="12" height="16" viewBox="0 0 12 16"><path d="M2 2l7 6-7 6" fill="none" stroke="#fff" stroke-width="3"/></svg>ONLINE QUOTE</h2>
    <span class="label" style="left:58px;top:87px">Choose your city</span>
    <span class="label" style="left:272px;top:88px">Duration</span>
    <ul class="cities">
      <li>Sydney</li><li>Melbourne</li><li>Gold Coast</li><li>Brisbane</li><li>Perth</li><li>Adelaide</li><li>Byron Bay</li>
    </ul>
    <div class="duration"></div>
    <a class="btn">GET A QUOTE NOW</a>
  </section>

  <section class="col deals">
    <h3>BEST DEALS</h3>
    <div class="deal"><span class="tag">Sydney</span>2 Semesters for $6,000*</div>
    <div class="deal"><span class="tag">Melbourne</span>2 Semesters for $6,000*</div>
    <div class="deal"><span class="tag">Gold Coast</span>2 Semesters for $6,000*</div>
    <div class="deal"><span class="tag">Brisbane</span>2 Semesters for $6,000*</div>
    <div class="deal"><span class="tag">Perth</span>2 Semesters for $6,000*</div>
    <div class="deal"><span class="tag">Adelaide</span>2 Semesters for $6,000*</div>
    <div class="deal"><span class="tag">Byron Bay</span>2 Semesters for $6,000*</div>
    <a class="more">Find out more</a>
  </section>

  <div class="divider" style="left:434px"></div>

  <section class="col ask">
    <h3>ASK US QUESTIONS</h3>
    <div class="ask-box">
      <p>Please ask us a question.</p>
      <div class="field"><span>Name:</span><i></i></div>
      <div class="field"><span>Email:</span><i></i></div>
      <div class="field"><span>Telephone:</span><i></i></div>
      <div class="field"><span>Question:</span><i></i></div>
      <a class="btn">SEND</a>
    </div>
  </section>

  <div class="divider" style="left:727px"></div>

  <section class="col links">
    <h3>QUICK LINKS</h3>
    <div class="link-item"><div class="thumb"></div><div><h4>Promotions</h4><p>Promotions promotionspromotions promoti</p><p>promotionsprom promotions.</p><a class="more">Find out more</a></div></div>
    <div class="link-item"><div class="thumb"></div><div><h4>Advantages</h4><p>Promotions promotionspromotions promoti</p><p>promotionsprom promotions.</p><a class="more">Find out more</a></div></div>
    <div class="link-item"><div class="thumb"></div><div><h4>Payment Option</h4><p>Promotions promotionspromotions promoti</p><p>promotionsprom promotions.</p><a class="more">Find out more</a></div></div>
  </section>
</main>

<footer class="footer">
  <div class="copy">
    © 2010 Lumora Estudos. All rights reserved.<br>
    <a>Privacy Policy</a><span class="sep">|</span><a>Terms and Conditions</a><span class="sep">|</span><a>FAQ</a><span class="sep">|</span><a>Contact Us</a>
  </div>
  <div class="partner" style="left:705px;width:90px"></div>
  <div class="partner" style="left:836px;width:122px"></div>
</footer>

</body>
</html>
```